Brookvale Insurance Services - Insurance Agency Wesbite

I need a website for my insurance agency called Brookvale Insurance Services. I have attached my company logo. You can use the colors from the copy logo to create the website color scheme. I need a Request A Quote section.
Business Address: 7316 Marlowe Ave Unit D, Studio City Ca 91607
Business Phone: (818) 555-0193
I would need the following drop downs on the main page:

1st drop down:
Business Insurance
⁃ Commercial Auto
⁃ Employment Practice Liability Insurance
⁃ General Liability Insurance
⁃ Professional Liability Insurance
⁃ Property Insurance
⁃ Workers Compensation Insurance

2nd drop down:
Industries We Serve
- Construction
- Janitorial
- Landscapers
- Trucking
- ParcelWay Independent Service Providers (ISP)
Healthcare Industry
- Community Care Facilities
- Home Health Agencies
- Hospice
- Nursing Homes

3rd drop down:
Risk Management
- Claims Management
- Compliance & Risk Management

4th drop down
Request a quote

5th drop down
About Us

6th drop down
Contact US

Target Market(s)

Potential clients

Industry/Entity Type

Business Insurance

Coding

Coded - Design and coding required

Number of Pages Required

5+ page

Colors
0054AA
0677BA
7BADD7
CADEEF
E8F1F8
00AB8E
00BBA5
67D7C9
C6EFE9
E9F9F6

Requirements
Must have
• Home Business Insurance - Commercial Auto - Employment Practice Liability Insurance - General Liability Insurance - Professional Liability Insurance - Property Insurance - Workers Compensation Insurance Industries We Serve - Construction - Janitorial - Landscapers - Manufacturing Companies - Restaurants - Towing - Trucking Healthcare Industry - Community Care Facilities - Home Health Agencies - Hospice - Nursing Homes - Risk Management - Claims Management - Compliance & Risk Management Request a Quote About Us Contact Us

```html
<!DOCTYPE html>
<html lang="en">
<head>
<meta charset="utf-8">
<title>Brookvale Insurance Services</title>
<link rel="stylesheet" href="https://fonts.googleapis.com/css2?family=Montserrat:wght@400;500;600;700;800&display=swap">
<style>
:root{
  --navy:#14298a;
  --blue:#0a3dc6;
  --green:#1c9b3c;
  --ink:#2c2f38;
  --muted:#555a66;
  --line:#d6d9df;
  --dark:#252a3b;
  --footer:#101114;
  --canvas:#eef0f3;
  --white:#ffffff;
}
*{box-sizing:border-box;margin:0;padding:0}
html,body{width:1200px;height:3162px;overflow:hidden}
body{background:var(--canvas);font-family:"Montserrat",sans-serif;color:var(--ink);padding-top:148px}
.page{width:1200px;background:var(--white);box-shadow:0 4px 30px rgba(0,0,0,.12)}

/* header */
.site-header{height:96px;display:flex;align-items:center;padding:0 59px 0 57px;justify-content:space-between}
.brand{font-weight:700;color:var(--navy);font-size:20px;letter-spacing:.5px;line-height:1.15;text-transform:uppercase}
.main-nav{display:flex;align-items:center;gap:0}
.main-nav a{font-size:13px;font-weight:500;color:var(--ink);text-decoration:none;margin-right:36px;letter-spacing:.3px}
.main-nav a.active{color:var(--green);border-bottom:2px solid var(--green);padding-bottom:2px}
.btn{display:inline-block;font-weight:600;font-size:12px;color:var(--white);text-decoration:none;text-align:center;letter-spacing:.3px;border:none}
.btn-quote{background:var(--green);width:165px;height:35px;line-height:35px;margin-left:-4px}

/* hero */
.hero{position:relative;height:598px;background:linear-gradient(100deg,#3a4a66 0%,#5d6f88 30%,#8b8f94 55%,#c7c1b6 75%,#9a9fa8 100%);overflow:hidden}
.hero::after{content:"";position:absolute;inset:0;background:rgba(28,52,110,.45)}
.hero-content{position:relative;z-index:1;text-align:center;padding-top:222px;color:var(--white)}
.hero-kicker{font-size:20px;font-weight:500;letter-spacing:.6px}
.hero-title{font-size:45px;font-weight:800;letter-spacing:1.5px;margin-top:8px}
.btn-hero{background:var(--blue);width:122px;height:34px;line-height:34px;margin-top:26px}

/* sections */
.section-title{text-align:center;color:var(--navy);font-weight:700;font-size:34px;letter-spacing:.5px;position:relative}
.section-title::after{content:"";display:block;width:44px;height:2px;background:var(--navy);margin:6px auto 0}

.services{height:670px;padding-top:82px;position:relative}
.card{position:absolute;background:var(--white);box-shadow:0 2px 14px rgba(0,0,0,.1);display:flex;padding:7px}
.card-photo{width:254px;flex:none}
.card-body{padding:14px 0 0 22px}
.card h3{color:var(--navy);font-size:19px;font-weight:700;line-height:1.12;text-transform:uppercase}
.card h3.green{color:var(--green)}
.card h4{color:var(--ink);font-size:14px;font-weight:600;margin:22px 0 6px 14px}
.card ul{list-style:none;margin-top:12px}
.card li{font-size:12px;line-height:1.75;color:var(--ink);padding-left:10px;position:relative}
.card li::before{content:"";position:absolute;left:0;top:7px;border-left:4px solid var(--ink);border-top:3px solid transparent;border-bottom:3px solid transparent}
.card li.wrap{line-height:1.2;padding-bottom:5px;padding-top:3px}
.card-business{left:60px;top:242px;width:524px;height:234px}
.card-risk{left:60px;top:508px;width:524px;height:156px}
.card-industries{left:614px;top:242px;width:526px;height:420px}
.arrow-badge{position:absolute;right:14px;top:14px;width:34px;height:34px}

/* about */
.about{height:592px;background:var(--dark);position:relative;color:var(--white);overflow:hidden}
.about-lines{position:absolute;inset:0}
.about-photo-main{position:absolute;left:60px;top:91px;width:351px;height:357px;border:2px solid var(--white);background:linear-gradient(135deg,#c8d3de,#7e93ad 60%,#46566f)}
.about-photo-gear{position:absolute;left:279px;top:270px;width:231px;height:230px;border:2px solid var(--white);background:radial-gradient(circle at 55% 45%,#2a8a9a,#0c2e45 70%,#081a2a)}
.dots{position:absolute;width:30px;height:90px;background-image:radial-gradient(#6e7488 1.3px,transparent 1.5px);background-size:10px 10px}
.about-text{position:absolute;left:616px;top:100px;width:520px}
.about-text h2{font-size:33px;font-weight:700;letter-spacing:.5px}
.about-text h2::after{content:"";display:block;width:52px;height:2px;background:var(--white);margin-top:2px}
.about-lead{font-size:16px;font-weight:700;line-height:1.45;margin-top:24px}
.about-text p.body{font-size:13px;line-height:1.5;color:#e3e5ea;margin-top:20px}
.btn-about{background:var(--green);width:121px;height:37px;line-height:37px;margin-top:34px}

/* quote */
.quote{height:576px;padding-top:82px}
.quote-form{width:577px;margin:42px auto 0;display:grid;grid-template-columns:278px 278px;column-gap:21px}
.field{margin-bottom:24px}
.field label{display:block;font-size:10px;font-weight:500;color:var(--ink);margin-bottom:5px;text-transform:uppercase}
.input{height:36px;border:1px solid var(--line);display:flex;align-items:center;padding:0 12px;justify-content:space-between}
.field-full{grid-column:1 / 3}
.textarea{height:96px;border:1px solid var(--line);padding:10px 12px}
.btn-submit{grid-column:1 / 3;justify-self:center;background:var(--blue);width:93px;height:35px;line-height:35px;margin-top:0}

/* footer */
.site-footer{height:294px;background:var(--footer);position:relative;color:var(--white)}
.footer-brand{position:absolute;left:59px;top:104px;width:214px;font-size:21px;text-align:center}
.footer-brand .brand{color:var(--white)}
.socials{position:absolute;left:96px;top:178px;display:flex;gap:16px;align-items:center}
.socials span{width:14px;height:14px;border-radius:50%;background:#d8dbe0}
.socials span.on{width:26px;height:26px;background:var(--green)}
.footer-col{position:absolute;top:80px}
.footer-col h5{color:var(--green);font-size:14px;font-weight:600;letter-spacing:.4px;margin-bottom:20px;text-transform:uppercase}
.contact-col{left:345px;width:270px}
.contact-row{display:flex;gap:10px;font-size:13px;line-height:1.35;margin-bottom:16px;color:#e8e9ec}
.contact-row svg{flex:none;margin-top:2px}
.links-col{left:667px}
.links-col a{display:block;color:#e8e9ec;text-decoration:none;font-size:13px;margin-bottom:15px}
.links-col a.active{color:var(--green);text-decoration:underline}
.footer-map{position:absolute;left:857px;top:76px;width:284px;height:149px;background:linear-gradient(135deg,#eef0ec,#dfe6ea 60%,#e9ede3)}
.to-top{position:absolute;right:-16px;top:238px}
.copyright{height:40px;background:var(--blue);color:var(--white);font-size:12px;text-align:center;line-height:40px}
</style>
</head>
<body>
<div class="page">

  <header class="site-header">
    <div class="brand">Brookvale Insurance Services</div>
    <nav class="main-nav">
      <a href="#" class="active">HOME</a>
      <a href="#">SERVICES</a>
      <a href="#">ABOUT US</a>
      <a href="#">CONTACT US</a>
      <a href="#" class="btn btn-quote">REQUEST A QUOTE</a>
    </nav>
  </header>

  <section class="hero" role="img" aria-label="Photo of a smiling agent and a client reviewing documents at a desk">
    <div class="hero-content">
      <div class="hero-kicker">BUILD AMAZING LIFE WITH</div>
      <h1 class="hero-title">BROOKVALE INSURANCE</h1>
      <a href="#" class="btn btn-hero">READ MORE</a>
    </div>
  </section>

  <section class="services">
    <h2 class="section-title">SERVICES</h2>

    <article class="card card-business">
      <div class="card-photo" role="img" aria-label="Photo of business colleagues meeting at an office table" style="background:linear-gradient(135deg,#d9dfe6,#8e9db2 55%,#2e3f63)"></div>
      <div class="card-body">
        <h3>Business<br>Insurance</h3>
        <ul>
          <li>Commercial Auto</li>
          <li>Commercial Property</li>
          <li class="wrap">Employment Practice Liability Insurance</li>
          <li>General Liability Insurance</li>
          <li>Professional Liability Insurance</li>
          <li>Workers Compensation Insurance</li>
        </ul>
      </div>
    </article>

    <article class="card card-risk">
      <div class="card-photo" role="img" aria-label="Photo of a hand stopping falling wooden blocks that spell risk" style="background:linear-gradient(135deg,#f2ece6,#d7b48e 55%,#b98a5c)"></div>
      <div class="card-body">
        <h3 class="green">Risk<br>Management</h3>
        <ul>
          <li>Claims Management</li>
          <li>Compliance &amp; Risk Management</li>
        </ul>
      </div>
      <svg class="arrow-badge" viewBox="0 0 34 34" aria-hidden="true">
        <circle cx="17" cy="17" r="17" fill="#1c9b3c"/>
        <path d="M13 21 L21 13 M15 13 H21 V19" stroke="#fff" stroke-width="2" fill="none"/>
      </svg>
    </article>

    <article class="card card-industries">
      <div class="card-photo" role="img" aria-label="Photo of a worker and a manager reviewing a tablet in a factory" style="background:linear-gradient(160deg,#cfd3d6,#8a8f94 50%,#3d4550)"></div>
      <div class="card-body">
        <h3>Industries<br>We Serve</h3>
        <ul>
          <li>Construction</li>
          <li class="wrap">ParcelWay Independent Service Providers (ISP)</li>
          <li>Janitorial</li>
          <li>Landscapers</li>
          <li>Manufacturing Companies</li>
          <li>Restaurants</li>
          <li>Towing</li>
          <li>Trucking</li>
        </ul>
        <h4>Healthcare Industry</h4>
        <ul style="margin-top:0">
          <li>Community Care Facilities</li>
          <li>Home Health Agencies</li>
          <li>Hospice</li>
          <li>Nursing Homes</li>
        </ul>
      </div>
    </article>
  </section>

  <section class="about">
    <svg class="about-lines" width="1200" height="592" aria-hidden="true">
      <g stroke="#2f3549" stroke-width="1" fill="none">
        <path d="M560 0 L760 300 L1000 40 L1200 320"/>
        <path d="M700 592 L900 330 L1200 520"/>
        <path d="M760 300 L900 330 L1000 40"/>
      </g>
    </svg>
    <div class="dots" style="left:420px;top:165px"></div>
    <div class="dots" style="left:240px;top:460px;height:50px"></div>
    <div class="about-photo-main" role="img" aria-label="Photo of a business team smiling around a laptop"></div>
    <div class="about-photo-gear" role="img" aria-label="Photo of a hand touching glowing digital gear icons"></div>
    <div class="about-text">
      <h2>ABOUT US</h2>
      <p class="about-lead">Brookvale Insurance Services stands as a full-service insurance brokerage committed to unparalleled service and exceptional value.</p>
      <p class="body">Our commitment extends to providing top-tier insurance products and resources, complemented by approachable and knowledgeable agents dedicated to delivering unparalleled customer service and ensuring client satisfaction.</p>
      <p class="body" style="margin-top:12px">From personal to professional services, we offer a broad spectrum of high-quality insurance coverage, with specialized experts in each domain to meet your unique needs. Trust us for a seamless experience that prioritizes your peace of mind.</p>
      <a href="#" class="btn btn-about">READ MORE</a>
    </div>
  </section>

  <section class="quote">
    <h2 class="section-title">REQUEST A QUOTE</h2>
    <form class="quote-form">
      <div class="field">
        <label>Name</label>
        <div class="input"><svg width="12" height="12" viewBox="0 0 12 12"><circle cx="6" cy="4" r="2.5" fill="none" stroke="#7a89b8"/><path d="M1.5 11.5 C2 8 10 8 10.5 11.5" fill="none" stroke="#7a89b8"/></svg></div>
      </div>
      <div class="field">
        <label>Phone Number</label>
        <div class="input"><svg width="10" height="12" viewBox="0 0 10 12"><rect x="2" y="0.5" width="6" height="11" rx="1" fill="none" stroke="#7a89b8"/></svg></div>
      </div>
      <div class="field">
        <label>Your Email</label>
        <div class="input"><svg width="12" height="10" viewBox="0 0 12 10"><rect x="0.5" y="0.5" width="11" height="9" fill="none" stroke="#7a89b8"/><path d="M0.5 0.5 L6 5 L11.5 0.5" fill="none" stroke="#7a89b8"/></svg></div>
      </div>
      <div class="field">
        <label>Services</label>
        <div class="input"><span></span><svg width="8" height="5" viewBox="0 0 8 5"><path d="M0 0 L8 0 L4 5Z" fill="#9aa0aa"/></svg></div>
      </div>
      <div class="field field-full">
        <label>Your Message</label>
        <div class="textarea"><svg width="11" height="11" viewBox="0 0 11 11"><path d="M0.5 0.5 H10.5 V7 L7 10.5 H0.5Z" fill="none" stroke="#7a89b8"/></svg></div>
      </div>
      <button type="button" class="btn btn-submit">SUBMIT</button>
    </form>
  </section>

  <footer class="site-footer">
    <div class="footer-brand"><div class="brand">Brookvale<br>Insurance Services</div></div>
    <div class="socials" aria-label="Social links">
      <span></span><span class="on"></span><span></span><span></span>
    </div>

    <div class="footer-col contact-col">
      <h5>Contact Info</h5>
      <div class="contact-row">
        <svg width="12" height="15" viewBox="0 0 12 15"><path d="M6 14 C2 9 1 7 1 5 A5 5 0 0 1 11 5 C11 7 10 9 6 14Z" fill="none" stroke="#1c9b3c" stroke-width="1.4"/><circle cx="6" cy="5" r="1.8" fill="#1c9b3c"/></svg>
        <span>7316 Marlowe Ave Unit D,<br>Studio City Ca 91607</span>
      </div>
      <div class="contact-row">
        <svg width="13" height="13" viewBox="0 0 13 13"><path d="M2 1 L4.5 1 L5.5 4 L4 5 C5 7.5 6 8.5 8 9 L9 7.5 L12 8.5 L12 11 C7 12 1 6 2 1Z" fill="none" stroke="#1c9b3c" stroke-width="1.3"/></svg>
        <span>(818) 555-0193</span>
      </div>
      <div class="contact-row">
        <svg width="13" height="11" viewBox="0 0 13 11"><rect x="0.7" y="0.7" width="11.6" height="9.6" fill="none" stroke="#1c9b3c" stroke-width="1.3"/><path d="M0.7 0.7 L6.5 5.5 L12.3 0.7" fill="none" stroke="#1c9b3c" stroke-width="1.3"/></svg>
        <span>info@brookvaleinsurance.com</span>
      </div>
    </div>

    <div class="footer-col links-col">
      <h5>Quick Link</h5>
      <a href="#" class="active">Home</a>
      <a href="#">Services</a>
      <a href="#">About Us</a>
      <a href="#">Contact Us</a>
    </div>

    <div class="footer-map" role="img" aria-label="Street map showing the office location in Studio City"></div>

    <svg class="to-top" width="36" height="36" viewBox="0 0 36 36" aria-label="Back to top">
      <circle cx="18" cy="18" r="18" fill="#0a3dc6"/>
      <path d="M18 25 V11 M12 17 L18 11 L24 17" stroke="#fff" stroke-width="2.2" fill="none"/>
    </svg>
  </footer>

  <div class="copyright">Copyright © Brookvale Insurance Services. All Rights Reserved</div>
</div>
</body>
</html>
```